Anime video website needs a creative design!

I run a site dedicated to Anime shows (Anime refers to Japanese cartoons). I need two pages designed for my site. A summary page, and a video page.

1) Now obviously, every show needs a distinct summary page, where people can read the show's plot summary, rate it if they like it, the number of episodes it has, its release date, and read other details about the show.

I need a new creative design for this summary page. I have attached the current design I'm working with - Try to keep all the information the current design has. But of course, you can remove things and change stuff. Like for example, no need for two ratings. And the episode list, you can remove thumbnails, or change the navigation somehow. Change the layout, put the image in the centre. It's your call. You can EVEN remove the sidebar and use the extra space and make the page full width.
But try sticking to the color scheme in the image.

In the image I've attached, I got the plot summary, cover image, etc from this site: http://toonvaultly.example/anime/19/Riverglass
I normally use this site to collect the show's information.

Of course, you can add things to the design as well, like thumbnails or screenhots of the show, etc if you feel like it. The space you have to work with is 800 pixels wide + 350 px for the sidebar. You have 1150 px if you're removing the sidebar.

2) Next I want you to design the video page, where people can watch clips of the show. I have attached the current design below. You don't have to design the video player. But you need to design the video tabs (above the video) - with some nice icons for HD maybe, the download buttons (below the video), the overall layout of the post. It MUST contain all the other information you designed in the previous page, like the rating, the plot, release date, etc.

Here, you have a width of 800 pixels to work with (ignoring the sidebar in the attached picture, the sidebar is like 350 pixels wide FYI). I'd prefer to not remove the sidebar, but again, if you want to you can remove it.

Looking forward to see what y'all can cook up!

P.S - You can change the design a lot. I don't mind a total redesign. Here are some different styles I found
1) http://qlnk.example/7TrXomA
2) http://qlnk.example/4GbeVuK (my current one - very plain :p)
3) http://qlnk.example/9JmoPzE

Target Market(s)

teenagers, young adults, entertainment, cartoons, animated movies

Number of Pages Required

2 page

Requirements
Must have
• Design must have two pages - one series page, one video page
Nice to have
• Nice fonts, icons, eye-catching design elements
• Try sticking to the current color scheme

```html
<!DOCTYPE html>
<html lang="en">
<head>
<meta charset="utf-8">
<title>Toon Harbor – Riverglass</title>
<link href="https://fonts.googleapis.com/css2?family=Open+Sans:wght@400;600;700;800&display=swap" rel="stylesheet">
<style>
:root{
  --red:#c8302a;
  --red-dark:#a8241f;
  --ink:#2b2b2b;
  --text:#555;
  --muted:#999;
  --line:#e3e3e3;
  --panel:#f4f4f4;
  --bg:#ffffff;
  --footer:#262626;
  --footer-text:#aaa;
}
*{box-sizing:border-box;margin:0;padding:0}
html,body{width:814px;height:1200px;overflow:hidden;background:var(--bg)}
body{font-family:"Open Sans",Arial,sans-serif;color:var(--text);font-size:6px;line-height:1.45}
.page{position:relative;width:814px;height:1200px}
.wrap{width:515px;margin:0 auto}

/* header */
.site-header{height:42px}
.site-header .wrap{height:100%;display:flex;align-items:center;justify-content:space-between}
.brand{display:flex;align-items:center;gap:5px}
.brand-mark{width:14px;height:14px;background:var(--red);border-radius:50%}
.brand-name{font-weight:800;font-size:12px;color:var(--red);letter-spacing:.4px}
.search{display:flex;width:120px;height:13px;border:1px solid var(--line)}
.search input{flex:1;min-width:0;border:0;font:inherit;font-size:5.5px;padding:0 4px;color:var(--muted);background:#fff}
.search button{width:14px;border:0;background:var(--red);display:flex;align-items:center;justify-content:center}

/* nav */
.main-nav{height:17px;background:var(--red)}
.main-nav .wrap{display:flex;height:100%}
.main-nav a{display:flex;align-items:center;padding:0 12px;color:#fff;text-decoration:none;font-weight:700;font-size:5.5px;letter-spacing:.3px;border-right:1px solid rgba(255,255,255,.18)}
.main-nav a.home{background:var(--red-dark);padding:0 9px}

/* hero */
.hero{position:relative;height:262px;overflow:hidden}
.hero-art{position:absolute;inset:0;background:linear-gradient(120deg,#1d2a44 0%,#5a4a62 35%,#8a6a70 55%,#3a3348 80%,#151a2a 100%)}
.hero-caption{position:absolute;left:0;right:0;top:112px;text-align:center;color:#fff}
.hero-caption h2{font-size:16px;font-weight:700;letter-spacing:.4px;line-height:1.2}
.hero-caption h3{font-size:11px;font-weight:700;letter-spacing:.3px;line-height:1.3}
.hero-caption p{font-size:5.5px;margin-top:2px;opacity:.85}
.hero-arrow{position:absolute;top:117px;width:14px;height:26px}
.hero-arrow.prev{left:170px}.hero-arrow.next{right:170px}
.hero-dots{position:absolute;bottom:6px;left:0;right:0;display:flex;justify-content:center;gap:3px}
.hero-dots span{width:4px;height:4px;border-radius:50%;background:rgba(255,255,255,.5)}
.hero-dots span.on{background:#fff}

/* layout */
.content{display:flex;justify-content:space-between;padding-top:22px}
.main{width:362px}
.sidebar{width:130px}

.section-title{font-size:8.5px;font-weight:700;color:var(--red);text-transform:uppercase;padding-bottom:4px;border-bottom:1px solid var(--line);margin-bottom:8px}
.section-title.dark{color:var(--ink)}

/* show */
.show{display:flex;gap:9px}
.show-poster{width:118px;height:138px;flex:none;background:linear-gradient(160deg,#3b4a6e,#7d5a64 60%,#c8302a)}
.show-plot h4{font-size:7px;color:var(--ink);font-weight:700;margin-bottom:2px}
.show-plot p{font-size:5px;line-height:1.5;margin-bottom:4px}
.show-meta{display:flex;justify-content:space-between;align-items:center;margin-top:8px}
.show-info{font-size:5px;line-height:1.8}
.show-info b{color:var(--red);font-weight:600}
.ratings{display:flex;gap:9px}
.rating{text-align:center;font-size:4.5px;color:var(--muted)}
.rating-ring{width:28px;height:28px;border:2px solid var(--red);border-radius:50%;display:flex;align-items:center;justify-content:center;font-weight:800;font-size:7px;color:var(--ink);margin:0 auto 2px}
.actions{display:flex;gap:6px;margin-top:6px}
.btn{display:flex;align-items:center;gap:4px;height:13px;padding:0 8px;font-size:5px;font-weight:700;color:#fff;text-transform:uppercase}
.btn.dark{background:var(--ink)}
.btn.red{background:var(--red)}

/* episodes */
.episodes{margin-top:30px}
.episode-grid{display:grid;grid-template-columns:repeat(3,1fr);gap:22px 12px}
.episode-thumb{position:relative;height:68px}
.episode-thumb svg{position:absolute;left:50%;top:50%;transform:translate(-50%,-50%)}
.ep1{background:linear-gradient(135deg,#2c3b5c,#7a8fb0)}
.ep2{background:linear-gradient(135deg,#5a4a3a,#c9a37a)}
.ep3{background:linear-gradient(135deg,#6a7a8a,#c9d3dc)}
.ep4{background:linear-gradient(135deg,#3a2a3a,#9a5a6a)}
.ep5{background:linear-gradient(135deg,#8a4a2a,#e0a060)}
.ep6{background:linear-gradient(135deg,#2a4a4a,#6aa0a0)}
.episode-label{font-size:6px;font-weight:700;color:var(--ink);margin-top:3px;line-height:1.3}
.episode-label small{display:block;font-weight:400;font-size:4.5px;color:var(--muted)}

/* comments */
.comments{margin-top:40px;border:1px solid var(--line)}
.comments-bar{display:flex;justify-content:space-between;align-items:center;height:15px;background:var(--panel);border-bottom:1px solid var(--line)}
.tabs{display:flex;height:100%}
.tabs span{display:flex;align-items:center;padding:0 10px;font-size:5.5px;font-weight:600;color:var(--muted)}
.tabs span.on{background:#fff;color:var(--ink);border-right:1px solid var(--line)}
.comments-tools{font-size:4.5px;color:var(--muted);padding-right:6px}
.comment-list{padding:4px 8px}
.comment{display:flex;gap:6px;padding:6px 0;border-bottom:1px solid var(--line)}
.comment:last-child{border-bottom:0}
.avatar{width:14px;height:14px;flex:none;background:#cfcfcf;border-radius:50%}
.comment b{display:block;font-size:5.5px;color:var(--red);font-weight:600}
.comment p{font-size:5px}

/* sidebar */
.widget{margin-bottom:12px}
.widget-head{background:var(--ink);color:#fff;font-size:6px;font-weight:700;padding:4px 7px;border-left:3px solid var(--red)}
.widget-head.red{background:var(--red);border-left-color:var(--red-dark)}
.widget-body{border:1px solid var(--line);border-top:0;padding:4px 7px}
.blog-item{padding:4px 0;border-bottom:1px dotted var(--line);font-size:5px}
.blog-item:last-child{border-bottom:0}
.blog-item b{display:block;color:var(--ink);font-weight:600}
.blog-item span{color:var(--muted);font-size:4.5px}
.sponsors{display:grid;grid-template-columns:1fr 1fr;gap:5px 6px;padding:7px}
.sponsors span{font-size:7px;font-weight:800;color:#777;text-transform:uppercase}
.recent-comment{font-size:5px;padding:4px 0;border-bottom:1px dotted var(--line)}
.recent-comment:last-child{border-bottom:0}
.social-box{border:1px solid var(--line);padding:5px}
.social-top{display:flex;gap:5px;align-items:center;font-size:5px;color:var(--ink);font-weight:600;line-height:1.3}
.social-top i{width:18px;height:18px;background:#ccc;display:block}
.social-fans{display:grid;grid-template-columns:repeat(6,1fr);gap:2px;margin-top:5px}
.social-fans i{height:14px;background:#d9d9d9;display:block}
.social-note{font-size:4.5px;color:var(--muted);margin-top:4px}
.ad{margin-top:120px;height:80px;background:linear-gradient(180deg,#1e3a6a,#284f8a);color:#fff;padding:7px;display:flex;flex-direction:column;justify-content:space-between}
.ad-name{font-size:12px;font-weight:800;line-height:1.1}
.ad-line{font-size:5.5px}
.ad-cta{align-self:flex-start;background:var(--red);font-size:5px;font-weight:700;padding:2px 6px}

/* footer */
.site-footer{position:absolute;left:0;right:0;bottom:0;height:72px;background:var(--footer);padding-top:22px}
.footer-row{display:flex;justify-content:space-between;align-items:center}
.footer-nav{font-size:5.5px;font-weight:700;color:#ddd;letter-spacing:.3px}
.footer-social{display:flex;gap:3px}
.footer-social i{width:11px;height:11px;background:#444;display:block}
.copyright{font-size:4.5px;color:var(--footer-text);margin-top:4px}
</style>
</head>
<body>
<div class="page">

  <header class="site-header">
    <div class="wrap">
      <div class="brand"><span class="brand-mark"></span><span class="brand-name">TOON HARBOR</span></div>
      <form class="search">
        <input type="text" value="Search here...">
        <button type="button" aria-label="Search">
          <svg width="7" height="7" viewBox="0 0 10 10"><circle cx="4" cy="4" r="3" fill="none" stroke="#fff" stroke-width="1.4"/><line x1="6.2" y1="6.2" x2="9" y2="9" stroke="#fff" stroke-width="1.4"/></svg>
        </button>
      </form>
    </div>
  </header>

  <nav class="main-nav">
    <div class="wrap">
      <a class="home" href="#" aria-label="Home">
        <svg width="8" height="7" viewBox="0 0 10 9"><path d="M5 0 L10 4.5 H8.5 V9 H6 V6 H4 V9 H1.5 V4.5 H0 Z" fill="#fff"/></svg>
      </a>
      <a href="#">CARTOONS</a><a href="#">ANIME SERIES</a><a href="#">ONGOING SERIES</a><a href="#">MOVIES</a><a href="#">STUFF</a><a href="#">FAQ</a>
    </div>
  </nav>

  <section class="hero">
    <div class="hero-art" role="img" aria-label="Illustrated banner of a large winged dragon against a dusky sky"></div>
    <div class="hero-caption">
      <h2>CUM NATOQUE PENATIBUS</h2>
      <h3>MAURIS VEL LACUS VITAE FELIS</h3>
      <p>Aenean commodo ligula eget dolor, sociis natoque magnis dis parturient montes.</p>
    </div>
    <svg class="hero-arrow prev" viewBox="0 0 14 26"><polyline points="11,3 3,13 11,23" fill="none" stroke="#fff" stroke-width="2.5"/></svg>
    <svg class="hero-arrow next" viewBox="0 0 14 26"><polyline points="3,3 11,13 3,23" fill="none" stroke="#fff" stroke-width="2.5"/></svg>
    <div class="hero-dots"><span class="on"></span><span></span><span></span><span></span></div>
  </section>

  <div class="wrap content">
    <main class="main">
      <h1 class="section-title">Riverglass</h1>
      <div class="show">
        <div class="show-poster" role="img" aria-label="Series cover art for Riverglass"></div>
        <div class="show-plot">
          <h4>Plot</h4>
          <p>In a canal city where every window is made of river glass, young glassblower Pell Arvane finds that the panes she shapes can hold reflections from days that have not happened yet. When her workshop's newest window shows the harbour bridge collapsing, she has one week to make someone believe her.</p>
          <p>Her warning draws the attention of the Lantern Guild, an old order that quietly collects such glass, and of a ferryman named Corso who claims he has seen the same vision in the water below his boat.</p>
          <p>Together they follow reflections through flooded archives, rooftop markets and a lighthouse nobody remembers building, learning that the city has been rewritten once before and that each pane Pell makes changes what comes next.</p>
          <p>As the week runs out, Pell must choose between saving the bridge and keeping the one reflection that shows her missing brother alive.</p>
        </div>
      </div>
      <div class="show-meta">
        <div class="show-info">
          <div><b>Alternative Titles:</b> Kawagarasu no Machi</div>
          <div><b>Genres:</b> Fantasy, Mystery, Drama, Adventure, Slice of Life</div>
          <div><b>Episodes:</b> 24 &nbsp; <b>Aired:</b> Jan 9, 2014 to Jun 19, 2014</div>
          <div><b>Status:</b> Finished Airing</div>
        </div>
        <div class="ratings">
          <div class="rating"><div class="rating-ring">87%</div>Site Rating</div>
          <div class="rating"><div class="rating-ring">75%</div>User Rating</div>
        </div>
      </div>
      <div class="actions">
        <span class="btn dark"><svg width="5" height="5" viewBox="0 0 8 8"><polygon points="1,0 8,4 1,8" fill="#fff"/></svg>Episode 1 English Dub</span>
        <span class="btn red"><svg width="5" height="5" viewBox="0 0 8 8"><polygon points="1,0 8,4 1,8" fill="#fff"/></svg>Episode 1 English Sub</span>
      </div>

      <section class="episodes">
        <h2 class="section-title dark">All Episodes</h2>
        <div class="episode-grid">
          <div><div class="episode-thumb ep1" role="img" aria-label="Still from episode 1"><svg width="16" height="16" viewBox="0 0 20 20"><circle cx="10" cy="10" r="9" fill="rgba(0,0,0,.45)" stroke="#fff"/><polygon points="8,6 14,10 8,14" fill="#fff"/></svg></div><div class="episode-label">Episode No. 1<small>The First Pane</small></div></div>
          <div><div class="episode-thumb ep2" role="img" aria-label="Still from episode 2"><svg width="16" height="16" viewBox="0 0 20 20"><circle cx="10" cy="10" r="9" fill="rgba(0,0,0,.45)" stroke="#fff"/><polygon points="8,6 14,10 8,14" fill="#fff"/></svg></div><div class="episode-label">Episode No. 2<small>Ferry at Dawn</small></div></div>
          <div><div class="episode-thumb ep3" role="img" aria-label="Still from episode 3"><svg width="16" height="16" viewBox="0 0 20 20"><circle cx="10" cy="10" r="9" fill="rgba(0,0,0,.45)" stroke="#fff"/><polygon points="8,6 14,10 8,14" fill="#fff"/></svg></div><div class="episode-label">Episode No. 3<small>The Lantern Guild</small></div></div>
          <div><div class="episode-thumb ep4" role="img" aria-label="Still from episode 4"><svg width="16" height="16" viewBox="0 0 20 20"><circle cx="10" cy="10" r="9" fill="rgba(0,0,0,.45)" stroke="#fff"/><polygon points="8,6 14,10 8,14" fill="#fff"/></svg></div><div class="episode-label">Episode No. 4<small>Flooded Archives</small></div></div>
          <div><div class="episode-thumb ep5" role="img" aria-label="Still from episode 5"><svg width="16" height="16" viewBox="0 0 20 20"><circle cx="10" cy="10" r="9" fill="rgba(0,0,0,.45)" stroke="#fff"/><polygon points="8,6 14,10 8,14" fill="#fff"/></svg></div><div class="episode-label">Episode No. 5<small>Rooftop Market</small></div></div>
          <div><div class="episode-thumb ep6" role="img" aria-label="Still from episode 6"><svg width="16" height="16" viewBox="0 0 20 20"><circle cx="10" cy="10" r="9" fill="rgba(0,0,0,.45)" stroke="#fff"/><polygon points="8,6 14,10 8,14" fill="#fff"/></svg></div><div class="episode-label">Episode No. 6<small>A Forgotten Light</small></div></div>
        </div>
      </section>

      <section class="comments">
        <div class="comments-bar">
          <div class="tabs"><span class="on">Comments</span><span>Toon Harbor</span></div>
          <div class="comments-tools">Share · Sort by Newest · Login</div>
        </div>
        <div class="comment-list">
          <div class="comment"><span class="avatar"></span><div><b>Mara Lindqvist</b><p>This series keeps getting better, the tension in the later episodes is unreal.</p></div></div>
          <div class="comment"><span class="avatar"></span><div><b>Theo Brandt</b><p>Finally a page with every episode in order. Thanks for the upload!</p></div></div>
          <div class="comment"><span class="avatar"></span><div><b>Jun Okafor</b><p>The dub is solid but I still prefer the sub for this one.</p></div></div>
        </div>
      </section>
    </main>

    <aside class="sidebar">
      <div class="widget">
        <div class="widget-head">Recent Blogs</div>
        <div class="widget-body">
          <div class="blog-item"><b>Top ten mystery series to watch</b><span>March 12, 2015</span></div>
          <div class="blog-item"><b>Spring season preview is here</b><span>March 08, 2015</span></div>
          <div class="blog-item"><b>Our favourite opening themes</b><span>March 02, 2015</span></div>
        </div>
      </div>
      <div class="widget">
        <div class="widget-head red">Sponsors</div>
        <div class="widget-body sponsors">
          <span>Lumeo</span><span>Brightwell</span><span>Orvix</span><span>Kestra</span>
        </div>
      </div>
      <div class="widget">
        <div class="widget-head">Recent Comments</div>
        <div class="widget-body">
          <div class="recent-comment">Mara on Riverglass Ep. 12</div>
          <div class="recent-comment">Theo on Spring preview</div>
          <div class="recent-comment">Jun on Opening themes</div>
          <div class="recent-comment">Lena on Riverglass Ep. 3</div>
          <div class="recent-comment">Ravi on Top ten mysteries</div>
        </div>
      </div>
      <div class="social-box">
        <div class="social-top"><i></i><span>Toon Harbor<br>Like Page</span></div>
        <div class="social-fans"><i></i><i></i><i></i><i></i><i></i><i></i><i></i><i></i><i></i><i></i><i></i><i></i></div>
        <div class="social-note">12,480 people like Toon Harbor</div>
      </div>
      <div class="ad" role="img" aria-label="Sports team advertisement">
        <div class="ad-name">Vantora</div>
        <div class="ad-line">Season tickets on sale now</div>
        <div class="ad-cta">BUY NOW</div>
      </div>
    </aside>
  </div>

  <footer class="site-footer">
    <div class="wrap">
      <div class="footer-row">
        <div class="footer-nav">HOME | CARTOONS | ANIME SERIES | ONGOING SERIES | MOVIES | STUFF | FAQ</div>
        <div class="footer-social"><i></i><i></i><i></i><i></i></div>
      </div>
      <div class="copyright">© 2015 Company Name. All right reserved. Terms of Use.</div>
    </div>
  </footer>

</div>
</body>
</html>
```